Kestrel Nine (IT/Network Services)

Kestrel Nine, LLC provides technology services to small and medium businesses. Essentially, anytime you've every thought your business might need an "IT guy" to handle something you could instead call us to handle it. Basically, you can outsource your IT needs to us.

This is a brand new company and so we'll need a brand new website. I'd like to use WordPress to handle the site since that will make things easier for me to maintain in the long run.

The site should include a, more-or-less, static front page with the dynamic data occurring on pages linked from a navigational area.

I have a logo already designed that I would like to see used in the design. The one with "white" in the title is the official logo, just added some other versions for your perusal.

Color queues from the logo but feel free to add other colors where applicable.

The site should feel somewhat corporate but with a "younger" slant (something a 25-35 year old would enjoy).

Pages (either to be added initially or by me after design completion):
"About" section - includes company history, business philosophy, etc.
"Services" section - service options, service approach, service specifics
"Testimonials" section - (eventually)
"News" section - (eventually) industry news, company news, events, blog
Contact Links

Websites to view:
The two largest local competitors:
http://www.brimfieldsystemsco.com/
http://www.qmworkset.com/
Other local competitors:
http://www.pvrllc.com/
http://www.lorvanassociates.com/

Other info you might find useful:
Domain: knllc.com
Address:
517 Hollis Row E
Suite 812B
Nashville, TN 37219
Phone: 615-382-7140
Emails available for use/display:
info@knllc.com
sales@knllc.com

Target Market(s)

Our target clients are mainly small businesses (25 or less computer users) which means we're looking at a lot of start-ups or younger companies. We'll be interacting with many entrepreneurs and young business owners.

Requirements
Must have
• Need full WP theme (not a mockup)

```html
<!DOCTYPE html>
<html lang="en">
<head>
<meta charset="utf-8">
<title>Kestrel Nine — IT &amp; Network Services</title>
<link rel="stylesheet" href="https://fonts.googleapis.com/css2?family=Signika:wght@400;600&family=Roboto+Condensed:wght@400;700&family=Arimo:wght@400;700&display=swap">
<style>
:root{
  --orange:#f08a14;
  --orange-deep:#e0470e;
  --orange-mid:#f6a01c;
  --nav:#7d8285;
  --nav-active:#63676a;
  --nav-line:#9a9ea1;
  --page:#e6e7e9;
  --band:#d2d3d5;
  --base:#c6c7c9;
  --ink:#5f6164;
  --body:#4a4b4d;
  --muted:#6d6f72;
  --blue:#1f5fc0;
  --blue-dark:#1a4fa3;
  --grey-num:#6b6e71;
  --news-date:#f06a10;
  --white:#ffffff;
  --logo:#d4d4d6;
}
*{box-sizing:border-box;margin:0;padding:0}
html,body{width:840px;height:1200px;overflow:hidden}
body{background:var(--page);font-family:"Arimo",Arial,sans-serif;color:var(--body);position:relative}
.abs{position:absolute}

/* hero */
.hero{left:0;top:0;width:840px;height:377px;
  background:radial-gradient(ellipse 60% 75% at 50% 45%,var(--orange-mid) 0%,var(--orange) 45%,var(--orange-deep) 100%);overflow:hidden}
.hero-photo{left:212px;top:32px;width:460px;height:345px;
  background:radial-gradient(ellipse 55% 60% at 40% 55%,rgba(235,235,235,.55) 0%,rgba(120,110,100,.25) 55%,rgba(240,138,20,0) 100%)}
.brand{left:82px;top:88px;display:flex;align-items:center;gap:8px}
.brand-dot{width:18px;height:18px;border-radius:50%;background:var(--logo)}
.brand-name{font-family:"Signika",sans-serif;font-weight:400;font-size:25px;color:var(--logo);letter-spacing:.5px}
.hero-title{left:424px;top:82px;font-family:"Signika",sans-serif;font-weight:600;font-size:36px;line-height:44px;color:var(--white);
  text-shadow:1px 2px 2px rgba(90,40,0,.55)}
.cta{left:427px;top:185px;width:179px;height:40px;background:var(--blue);border:3px solid var(--white);
  color:var(--white);font-family:"Signika",sans-serif;font-weight:600;font-size:18px;line-height:34px;text-align:center}

/* nav */
.main-nav{left:0;top:377px;width:840px;height:34px;background:var(--nav)}
.nav-list{left:79px;top:0;display:flex;list-style:none;height:34px}
.nav-list li{font-family:"Roboto Condensed",sans-serif;font-weight:700;font-size:14px;color:var(--white);
  line-height:34px;text-align:center;border-right:1px solid var(--nav-line)}
.nav-list li.active{background:var(--nav-active);color:#3f4245}
.search{left:602px;top:6px;width:161px;height:23px;background:var(--white);display:flex}
.search span{flex:1;font-size:11px;color:#8a8c8f;line-height:23px;padding-left:8px}
.search-btn{width:23px;height:23px;background:var(--blue)}

/* intro */
.section-title{font-family:"Signika",sans-serif;font-weight:600;font-size:21px;color:var(--ink);line-height:24px}
.intro-title{left:78px;top:450px;width:440px}
.steps{left:78px;top:516px;width:430px;list-style:none}
.step{display:flex;gap:14px;margin-bottom:14px;align-items:center}
.step-num{flex:none;width:34px;height:34px;border-radius:50%;color:var(--white);font-family:"Signika",sans-serif;
  font-size:19px;font-weight:600;text-align:center;line-height:32px;border:2px solid #f4f4f4;box-shadow:0 1px 2px rgba(0,0,0,.3)}
.n1{background:var(--blue)}.n2{background:var(--orange-deep)}.n3{background:var(--grey-num)}
.step p{font-size:10.3px;line-height:13px;color:var(--body)}
.news-title{left:541px;top:452px}
.news{left:541px;top:482px;width:215px;list-style:none}
.news li{margin-bottom:12px;font-size:9.6px;line-height:12.5px}
.news-date{display:block;color:var(--news-date);text-decoration:underline}

/* services */
.services{left:78px;top:706px;width:700px;height:230px}
.service{position:absolute;top:0;width:160px}
.service-icon{width:52px;height:52px;margin-left:52px;border-radius:8px}
.i1{background:radial-gradient(circle at 40% 35%,#9fb0c6,#3b4c6a)}
.i2{background:linear-gradient(135deg,#f2a93a,#8b8d90)}
.i3{background:linear-gradient(135deg,#c04a2a,#b9bcbf)}
.i4{background:radial-gradient(circle at 40% 35%,#7fb4f0,#1847a3)}
.service h3{font-family:"Signika",sans-serif;font-weight:600;font-size:19px;color:var(--ink);margin-top:18px;line-height:22px;white-space:nowrap}
.service p{font-size:9.6px;line-height:14px;margin-top:4px;color:var(--body)}
.btn{position:absolute;top:202px;width:68px;height:24px;border:1px solid #c9cacc;border-radius:3px;background:linear-gradient(#fafafa,#e8e8e8);
  font-size:9.5px;font-weight:700;color:var(--muted);text-align:center;line-height:22px}
.btn-primary{background:linear-gradient(#2f8ae0,#1f4fb0);color:var(--white);border-color:#1a3f8f}

/* support band */
.support{left:0;top:976px;width:840px;height:149px;background:var(--band)}
.support-title{left:78px;top:20px}
.links{top:64px;width:112px;list-style:none}
.links li{font-size:8.8px;color:var(--muted);height:21px;line-height:20px;border-bottom:1px dotted #a5a7aa;padding-left:10px;position:relative}
.links li::before{content:"";position:absolute;left:0;top:7px;border-left:5px solid #8e9093;border-top:3px solid transparent;border-bottom:3px solid transparent}
.signup-title{left:541px;top:20px}
.signup-text{left:541px;top:54px;width:220px;font-size:8.8px;line-height:13px;color:var(--body)}
.signup-field{left:541px;top:100px;width:142px;height:25px;background:var(--white);font-size:10px;color:var(--muted);line-height:25px;padding-left:9px}
.signup-btn{left:688px;top:100px;width:73px;height:25px;background:var(--blue);color:var(--white);font-family:"Signika",sans-serif;font-weight:600;font-size:13px;text-align:center;line-height:25px}

/* base */
.base{left:0;top:1125px;width:840px;height:75px;background:var(--base);border-top:4px solid #a9abae}
.legal{left:78px;top:20px;font-size:8.6px;color:var(--muted);line-height:17px}
.social{left:643px;top:18px;display:flex;gap:8px;list-style:none}
.social li{width:25px;height:25px;border-radius:4px;background:linear-gradient(#fafafa,#dcdcdc);border:1px solid #b5b7b9}
</style>
</head>
<body>

<header class="hero abs">
  <div class="hero-photo abs" role="img" aria-label="Photo of a young man in a white shirt working on a laptop"></div>
  <div class="brand abs"><span class="brand-dot"></span><span class="brand-name">Kestrel Nine</span></div>
  <h1 class="hero-title abs">Does your business<br>needs an “IT Guy?”</h1>
  <div class="cta abs">CONTACT US NOW</div>
</header>

<nav class="main-nav abs">
  <ul class="nav-list abs">
    <li class="active" style="width:62px">HOME</li>
    <li style="width:87px">ABOUT US</li>
    <li style="width:83px">SERVICES</li>
    <li style="width:97px">TESTIMONAL</li>
    <li style="width:72px">NEWS</li>
    <li style="width:99px">CONTACT US</li>
  </ul>
  <div class="search abs"><span>Search...</span>
    <div class="search-btn"><svg width="23" height="23" viewBox="0 0 23 23"><circle cx="12.5" cy="9.5" r="4.5" fill="none" stroke="#fff" stroke-width="2"/><line x1="9.3" y1="12.7" x2="5.5" y2="16.5" stroke="#fff" stroke-width="2.4"/></svg></div>
  </div>
</nav>

<h2 class="section-title intro-title abs">What we can do for you through Information Technology:</h2>
<ol class="steps abs">
  <li class="step"><span class="step-num n1">1</span><p>Mam libero tempore massasoluta nobis est eligendi omnis voluassumenda est, omnis dolo- resereeledusempquibusdamet aurerum odes necessitatibus saepe eveniet utoluptates estu</p></li>
  <li class="step"><span class="step-num n2">2</span><p>Sibero tempore massasoluta nobis est eligendi omnis voluassumenda est, omnis dolore- sereeledusempquibusdamet aurerum odes necessitatibus saepe eveniet utoluptates estu repudiandae sintet molestiae non recusandaeltaque earum.</p></li>
  <li class="step"><span class="step-num n3">3</span><p>Mam libero tempore massasoluta nobis est eligendi omnis voluassumenda est, omnis dolo- resereeledusempquibusdamet aurerum odes necessitatibus saepe eveniet utoluptates estu</p></li>
</ol>

<h2 class="section-title news-title abs">Kestrel Nine Latest News:</h2>
<ul class="news abs">
  <li><span class="news-date">20.05.2012:</span>massasoluta nobis est eligendi omnis voluassumenda est, omnis doloreser-eeledusempquibusdamet aurerum odesom</li>
  <li><span class="news-date">20.05.2012:</span>massasoluta nobis est eligendi<br>omnis voluassumenda est, omnis doloreser-eeledusempquibusdamet aurerum odes nece</li>
  <li><span class="news-date">20.05.2012:</span>massasoluta nobis est eligendi omnis voluassumenda est, omnis doloreser-eeledusempquibusdamet aurerum odesom</li>
</ul>

<section class="services abs">
  <article class="service" style="left:0">
    <div class="service-icon i1" role="img" aria-label="Globe network icon"></div>
    <h3>Networking</h3>
    <p>Mam libero tempore massasoluta nobis est eligendi omnis voluasas sumenda est, omnis dolorLesereele dusempquibusdamet aurerum odes necessitatibus saepe eveniet uto luptates estu repudiandae sint et molestiae.</p>
  </article>
  <div class="btn btn-primary" style="left:0">Read More</div>
  <article class="service" style="left:170px">
    <div class="service-icon i2" role="img" aria-label="Wrench and hammer icon"></div>
    <h3>Technical Support</h3>
    <p>Mam libero tempore massasoluta nobis est eligendi omnis voluasas sumenda est, omnis dolorLesereele dusempquibusdamet aurerum odes necessitatibus saepe eveniet uto luptates estu repudiandae sint et molestiae.</p>
  </article>
  <div class="btn" style="left:170px">Read More</div>
  <article class="service" style="left:340px">
    <div class="service-icon i3" role="img" aria-label="Drafting tools icon"></div>
    <h3>Project Management</h3>
    <p>Mam libero tempore massasoluta nobis est eligendi omnis voluasas sumenda est, omnis dolorLesereele dusempquibusdamet aurerum odes necessitatibus saepe eveniet uto luptates estu repudiandae sint et molestiae.</p>
  </article>
  <div class="btn" style="left:340px">Read More</div>
  <article class="service" style="left:530px">
    <div class="service-icon i4" role="img" aria-label="Globe with screwdriver icon"></div>
    <h3>IT Solutions</h3>
    <p>Mam libero tempore massasoluta nobis est eligendi omnis voluasas sumenda est, omnis dolorLesereele dusempquibusdamet aurerum odes necessitatibus saepe eveniet uto luptates estu repudiandae sint et molestiae.</p>
  </article>
  <div class="btn" style="left:530px">Read More</div>
</section>

<section class="support abs">
  <h2 class="section-title support-title abs">IT Support and Assistance Services</h2>
  <ul class="links abs" style="left:78px"><li>Proactive IT Support</li><li>Business Continuity</li><li>Disaster Recover</li></ul>
  <ul class="links abs" style="left:227px"><li>IT Network Support</li><li>Managed IT Services</li><li>ICT Support</li></ul>
  <ul class="links abs" style="left:375px"><li>IT Audit</li><li>Office Relocation</li><li>IT General Support</li></ul>
  <h2 class="section-title signup-title abs">Newsletter Sign Up</h2>
  <p class="signup-text abs">Aliquam congue fermentum nisl. Mauris accumsan nulla vel diam. Sed in lacus ut enim.</p>
  <div class="signup-field abs">Email Address:</div>
  <div class="signup-btn abs">Subscribe</div>
</section>

<footer class="base abs">
  <p class="legal abs">Kestrel Nine © Copyright 2012 | Privacy Policy<br>Home &nbsp;|&nbsp; About Us &nbsp;|&nbsp; Services &nbsp;|&nbsp; Testimonial &nbsp;|&nbsp; News &nbsp;|&nbsp; Contact Us</p>
  <ul class="social abs" aria-label="Social links"><li></li><li></li><li></li><li></li></ul>
</footer>

</body>
</html>
```